Trevor Outreach Group's Primary Marketing Brochure (Gate Fold Format)

We are looking for a main brochure design to communicate our company's primary mission, the need, where we meet the needs, how we meet the needs, and how the reader can get involved. We would like to see the color palette be similar to the colors of our company logo (attached). We would like to see a brochure design similar to a "gate fold" offering 22"x8.5" fully opened and 5.5"x8.5" when closed. Front panel, inside panels, full spread panel, and back panel. Required Text for each panel and usable picture suggestions are attached along with the company logo. The design should clean, contemporary, and emotionally compelling.

Target Market(s)

40-65 years old male and female, religious-minded

Industry/Entity Type

It Company

Font styles to use
Sans Serif

Requirements
Must have
• include text from attached WORD document.
• Clean, contemporary design
• Color in color palette of agency logo attached

```html
<!DOCTYPE html>
<html lang="en">
<head>
<meta charset="utf-8">
<title>Trevor Outreach Group – Gate Fold Brochure</title>
<link rel="stylesheet" href="https://fonts.googleapis.com/css2?family=Libre+Baskerville:wght@400;700&family=Lato:wght@400;700&display=swap">
<style>
  :root {
    --navy: #2a4596;
    --navy-deep: #223a84;
    --gold: #b59a5f;
    --gold-light: #c9b27a;
    --paper: #ffffff;
    --backdrop: #ececec;
    --ink: #3b3f52;
    --mist: #e9eaee;
  }
  * { box-sizing: border-box; margin: 0; padding: 0; }
  html, body { width: 1200px; height: 1200px; overflow: hidden; }
  body {
    background: var(--backdrop);
    font-family: "Lato", Arial, sans-serif;
    color: var(--ink);
    position: relative;
  }
  .spread {
    position: absolute;
    left: 40px; top: 383px;
    width: 1120px; height: 433px;
    display: flex;
    background: var(--paper);
  }
  .gate {
    position: relative;
    width: 280px; height: 433px;
    overflow: hidden;
    background: var(--paper);
  }
  .gate--left { border-right: 1px solid #e3e3e6; }
  .gate--right { border-left: 1px solid #e3e3e6; }
  .cover {
    position: absolute;
    top: 0;
    width: 560px; height: 433px;
  }
  .gate--left .cover { left: -280px; }
  .gate--right .cover { left: 0; }

  .brand {
    position: absolute;
    left: 0; right: 0; top: 26px;
    display: flex; justify-content: center; align-items: center; gap: 8px;
  }
  .brand__name {
    font-family: "Lato", Arial, sans-serif;
    font-weight: 700;
    font-size: 22px;
    color: var(--navy);
    white-space: nowrap;
  }
  .brand__dot {
    width: 26px; height: 26px;
    border-radius: 50%;
    background: var(--navy);
  }
  .cover__photo {
    position: absolute;
    left: 132px; top: 100px;
    width: 296px; height: 296px;
    border-radius: 50%;
    border: 3px solid var(--gold);
    background: linear-gradient(180deg, #8e9db1 0%, #4f6b8f 35%, #b64a45 58%, #3c4e74 80%, #6b6a5d 100%);
  }
  .cover__wave { position: absolute; left: 0; top: 0; }
  .cover__title {
    position: absolute;
    left: 0; right: 0; top: 358px;
    text-align: center;
    font-family: "Libre Baskerville", Georgia, serif;
    font-weight: 700;
    font-size: 19px;
    line-height: 26px;
    color: #ffffff;
    letter-spacing: 0.5px;
  }
  .cover__title .gold {
    display: block;
    color: var(--gold-light);
    font-weight: 400;
  }
  .cover__url {
    position: absolute;
    left: 0; right: 0; top: 418px;
    text-align: center;
    font-size: 7.5px;
    letter-spacing: 4px;
    color: #ffffff;
  }

  .inside {
    position: relative;
    width: 560px; height: 433px;
    background: var(--paper);
  }
  .vision {
    position: absolute;
    left: 16px; right: 22px; top: 28px;
    font-size: 5.6px; line-height: 1.45;
  }
  .label {
    color: var(--navy);
    display: flex; align-items: center; gap: 3px;
    font-size: 5.8px;
  }
  .label::before, .faith li::before {
    content: ""; width: 3.5px; height: 3.5px; border-radius: 50%;
    border: 1px solid var(--navy); flex: none;
  }
  .vision p { margin: 1px 0 5px 7px; }
  .rule {
    position: absolute; left: 0; right: 0;
    height: 1.5px; background: var(--navy);
  }
  .rule--top { top: 112px; }
  .rule--bottom { top: 288px; }
  .tab {
    position: absolute;
    left: 230px; top: 104px;
    width: 100px; height: 16px;
    border-radius: 8px;
    background: var(--gold);
    color: #fff;
    font-family: "Libre Baskerville", Georgia, serif;
    font-size: 8.5px;
    line-height: 16px;
    text-align: center;
  }
  .faith {
    position: absolute;
    top: 136px; left: 16px; right: 20px;
    display: flex; gap: 28px;
  }
  .faith ul { list-style: none; flex: 1; }
  .faith li {
    display: flex; gap: 4px;
    font-size: 5.4px; line-height: 1.5;
    margin-bottom: 3px;
    text-align: justify;
  }
  .faith li::before { margin-top: 2px; }
  .backdrop-photo {
    position: absolute;
    left: 0; right: 0; top: 290px; bottom: 0;
    background: linear-gradient(180deg, #f3f3f5 0%, var(--mist) 45%, #f4f4f6 100%);
  }
  .footer-brand {
    position: absolute;
    top: 334px; left: 0; right: 0;
    display: flex; justify-content: center; align-items: center; gap: 18px;
  }
  .footer-brand .brand__name { font-size: 17px; }
  .footer-brand .brand__dot { width: 20px; height: 20px; }
  .badge {
    width: 34px; height: 34px; border-radius: 50%;
    background: var(--navy);
    border: 3px solid #cfd3de;
  }
  .contact {
    position: absolute;
    left: 0; right: 0; top: 418px;
    display: flex; justify-content: center; gap: 12px;
    font-size: 5.4px; color: var(--ink);
  }
  .contact span { display: flex; align-items: center; gap: 3px; }
  .contact svg { width: 6px; height: 6px; fill: var(--navy); }
</style>
</head>
<body>
<main class="spread">

  <section class="gate gate--left">
    <div class="cover">
      <div class="brand"><span class="brand__name">Trevor Outreach Group</span><span class="brand__dot"></span></div>
      <div class="cover__photo" role="img" aria-label="Photo of a group of children holding red Bibles in front of a school building"></div>
      <svg class="cover__wave" width="560" height="433" viewBox="0 0 560 433">
        <path d="M0,322 C120,320 200,344 300,338 C400,332 470,318 560,322 L560,433 L0,433 Z" fill="#b59a5f"/>
        <path d="M0,330 C120,328 200,352 300,346 C400,340 470,326 560,330 L560,433 L0,433 Z" fill="#2a4596"/>
      </svg>
      <h1 class="cover__title">EQUIPPING THE NATIONS<span class="gold">WITH THE GOSPEL</span></h1>
      <div class="cover__url">www.trevoroutreach.org</div>
    </div>
  </section>

  <section class="inside">
    <div class="vision">
      <div class="label">Vision of Trevor Outreach Group</div>
      <p>Our vision is ever more communities all around the world radically transformed by the love of the Gospel: communities with reproducing, multiplying, Christ-centered national leaders who are part of thriving, engaged local churches growing committed disciples of Jesus, boldly proclaiming the Good News, compassionately caring for spiritual and physical needs, and advancing the Kingdom in all aspects of society.</p>
      <div class="label">Statement of Faith</div>
    </div>

    <div class="rule rule--top"></div>
    <div class="tab">We believe:</div>

    <div class="faith">
      <ul>
        <li>In the Scriptures of the Old and New Testament as inspired by God and inerrant in the original writings, the supreme and final authority in faith and life.</li>
        <li>In one God, eternally existing in three persons: Father, Son, and Holy Spirit.</li>
        <li>That Jesus Christ was begotten by the Holy Spirit and born of the virgin Mary, and is true God and true man.</li>
        <li>That man was created in the image of God, that he sinned and thereby incurred both physical and spiritual death, and that all are born with a sinful nature.</li>
        <li>That the Lord Jesus Christ died for our sins as a representative and substitutionary sacrifice, and all who believe in Him are justified by His shed blood.</li>
      </ul>
      <ul>
        <li>In the bodily resurrection of our crucified Lord, His ascension into heaven and His presence there for us as High Priest and Advocate.</li>
        <li>In that blessed hope, the personal and victorious return of our Lord and Savior, Jesus Christ.</li>
        <li>That all who receive by repentance and faith the Lord Jesus Christ are born again of the Holy Spirit and become children of God.</li>
        <li>In the bodily resurrection of the just and unjust, the everlasting blessedness of the saved and the everlasting punishment of the lost.</li>
        <li>That God created man and woman as unique persons made to complete each other, and that marriage between one man and one woman is the foundation of the family and of society.</li>
      </ul>
    </div>

    <div class="rule rule--bottom"></div>
    <div class="backdrop-photo" role="img" aria-label="Faint background photo of a child"></div>

    <div class="footer-brand">
      <div style="display:flex;align-items:center;gap:6px"><span class="brand__name">Trevor Outreach Group</span><span class="brand__dot"></span></div>
      <span class="badge" role="img" aria-label="Accreditation badge"></span>
    </div>

    <div class="contact">
      <span><svg viewBox="0 0 10 10"><path d="M5 0a3.5 3.5 0 0 0-3.5 3.5C1.5 6 5 10 5 10s3.5-4 3.5-6.5A3.5 3.5 0 0 0 5 0zm0 5a1.4 1.4 0 1 1 0-2.8A1.4 1.4 0 0 1 5 5z"/></svg>1420 Harbor Lane, Millbrook, Tennessee, TN 37000</span>
      <span><svg viewBox="0 0 10 10"><path d="M2 0.5l2 2-1 1.3c.6 1.3 1.6 2.3 2.9 2.9L7.2 5.7l2 2L8 9.5C4 9.5.5 6 .5 2z"/></svg>1-800-555-0142</span>
      <span><svg viewBox="0 0 10 10"><circle cx="5" cy="5" r="4.3" fill="none" stroke="#2a4596" stroke-width="1.2"/><path d="M0.7 5h8.6" stroke="#2a4596" stroke-width="1"/></svg>www.trevoroutreach.org</span>
      <span><svg viewBox="0 0 10 10"><rect width="10" height="10" rx="2"/></svg>/trevoroutreach</span>
      <span><svg viewBox="0 0 10 10"><circle cx="5" cy="5" r="5"/></svg>@TREVOROG</span>
    </div>
  </section>

  <section class="gate gate--right">
    <div class="cover">
      <div class="brand"><span class="brand__name">Trevor Outreach Group</span><span class="brand__dot"></span></div>
      <div class="cover__photo" role="img" aria-label="Photo of a group of children holding red Bibles in front of a school building"></div>
      <svg class="cover__wave" width="560" height="433" viewBox="0 0 560 433">
        <path d="M0,322 C120,320 200,344 300,338 C400,332 470,318 560,322 L560,433 L0,433 Z" fill="#b59a5f"/>
        <path d="M0,330 C120,328 200,352 300,346 C400,340 470,326 560,330 L560,433 L0,433 Z" fill="#2a4596"/>
      </svg>
      <h1 class="cover__title">EQUIPPING THE NATIONS<span class="gold">WITH THE GOSPEL</span></h1>
      <div class="cover__url">www.trevoroutreach.org</div>
    </div>
  </section>

</main>
</body>
</html>
```